Keystone Perks Supplier Statement

We want to design a better look and feel for the attached report. It has to look like the corporate website, match colours and stand out in the eyes of our customers that will receive this report every month. Big numbers and phrase. There has to be a header, nice graphs (you can point the concept we create the graphs with the real numbers) a space for marketing message (banner), space for opportunities (list of top shops) after that shop list details as in the report. www.vrelto.com for reference. This report is focused on our Loyalty program at www.vrelto.com/rewards. Use the references for the Loyalty Program.
This design is intended to be converted into a monthly html email statement for our participating Rewards Suppliers.

Target Market(s)

Automotive industry, Automotive OEM Supplier

Industry/Entity Type

Oem Supplier

Font styles to use
Other font styles liked:
• Roboto

Requirements
Must have
• Follow the Corporate Colors from the website and logo. Cannot have anything different than the corporate colours. The Keystone Perks logo shall use the following colors: Color - red (Pantone 485 C) and black (100% Black)
Nice to have
• work with images provided.

```html
<!DOCTYPE html>
<html lang="en">
<head>
<meta charset="utf-8">
<title>Keystone Perks – Supplier Points Statement</title>
<link href="https://fonts.googleapis.com/css2?family=Roboto:wght@300;400;500;700;900&display=swap" rel="stylesheet">
<style>
:root{
  --red:#d50f2f;
  --red-dark:#a8261b;
  --orange:#e8632c;
  --gold:#e9ae3a;
  --black:#111;
  --ink:#2b2b2b;
  --muted:#666;
  --line:#d6d6d6;
  --panel:#f2f2f2;
  --band:#262626;
  --bg:#9a9a9a;
}
*{box-sizing:border-box;margin:0;padding:0}
html,body{width:1200px;height:1200px;overflow:hidden;background:var(--bg);font-family:'Roboto',Arial,sans-serif;color:var(--ink)}
.stage{position:absolute;left:0;top:0;width:1500px;height:1500px;transform:scale(.8);transform-origin:0 0}
.page{position:absolute;top:292px;width:648px;height:916px;background:#fff;overflow:hidden}
.page--cover{left:79px}
.page--summary{left:774px}
.abs{position:absolute}
.footer{position:absolute;left:0;right:0;bottom:0;background:var(--red)}
.page--cover .footer{height:75px}
.page--summary .footer{height:124px}
.footer-contact{position:absolute;left:57px;color:#fff;font-size:13px;white-space:nowrap}
.footer-contact small{display:block;font-size:9px;letter-spacing:.3px;margin-bottom:3px}
.footer-contact b{color:#111;font-weight:500}
.footer-brand{position:absolute;display:flex;align-items:center;gap:6px;color:#111}
.brand-dot{width:30px;height:30px;border-radius:50%;background:#111}
.brand-name{font-weight:900;font-size:13px;line-height:1;letter-spacing:1px;color:#111}
.brand-sep{width:1px;height:22px;background:#fff;margin:0 4px}
.brand-url{color:#fff;font-weight:700;font-size:11px}
.header-brand{position:absolute;left:172px;top:18px;display:flex;align-items:center;gap:10px}
.header-dot{width:74px;height:74px;border-radius:50%;background:var(--red)}
.header-name{font-weight:900;font-size:32px;line-height:1;letter-spacing:1px;color:var(--black)}
.photo{position:absolute}
.title-band{position:absolute;left:0;top:262px;width:490px;height:137px;background:var(--band);color:#fff;display:flex;align-items:center;padding-left:40px;font-size:20px;font-weight:400;letter-spacing:.3px}
.section-title{position:absolute;left:0;right:0;text-align:center;color:var(--red);font-weight:700;font-size:13px}
.section-title span{color:var(--ink)}
.section-sub{position:absolute;left:0;right:0;text-align:center;font-size:12px;color:var(--ink)}
.card{position:absolute;background:var(--panel);border-radius:12px;box-shadow:0 2px 4px rgba(0,0,0,.18)}
.card-title{position:absolute;left:0;right:0;text-align:center;font-size:9px;color:var(--ink)}
table{border-collapse:collapse;width:100%;table-layout:fixed}
.data-table{position:absolute;border-radius:10px;overflow:hidden;background:#fff;box-shadow:0 0 0 1px var(--line),0 2px 3px rgba(0,0,0,.15)}
.franchise-table th{background:var(--band);color:#fff;font-size:8px;font-weight:700;height:31px;text-align:center}
.franchise-table th.left{text-align:left;padding-left:10px;font-size:7px;line-height:1.1}
.franchise-table td{font-size:7px;height:19px;text-align:center;border-right:1px solid #eee;font-weight:500}
.franchise-table td.label{text-align:right;padding-right:6px;border:0}
.franchise-table td.brand{text-align:left;padding-left:10px;border:0}
.market-table th{background:#e7e7e7;font-size:8px;font-weight:500;height:22px;border-right:1px solid #fff}
.market-table th.left{text-align:left;padding-left:15px;font-size:7px}
.market-table td{font-size:7px;font-weight:500;text-align:center;height:22px;border-right:1px solid #eee;border-top:1px solid #e4e4e4}
.market-table td.left{text-align:left;padding-left:15px}
.shop-table th{background:#e7e7e7;font-size:7px;font-weight:700;height:20px;border-right:1px solid #d0d0d0}
.shop-table th.left{text-align:left;padding-left:14px}
.shop-table td{font-size:7px;height:16.2px;border-top:1px solid #e4e4e4;border-right:1px solid #ddd;text-align:center;color:#444}
.shop-table td.left{text-align:left;padding-left:14px}
svg text{font-family:'Roboto',Arial,sans-serif}
</style>
</head>
<body>
<div class="stage">

  <section class="page page--cover">
    <div class="header-brand">
      <div class="header-dot"></div>
      <div class="header-name">KEYSTONE PERKS</div>
    </div>

    <div class="photo" style="left:0;top:101px;width:328px;height:158px;background:linear-gradient(135deg,#2a2a2a,#6b6b6b 55%,#1c1c1c)" role="img" aria-label="Close-up of car climate control dials"></div>
    <div class="photo" style="left:330px;top:101px;width:160px;height:158px;background:radial-gradient(circle at 50% 45%,#fafafa 0 45%,#d8d8d8 60%,#e7c7c7)" role="img" aria-label="Wall clock over a calendar page"></div>
    <div class="photo" style="left:493px;top:101px;width:155px;height:158px;background:linear-gradient(135deg,#e9e9e9,#8d8d8d 50%,#c9c9c9)" role="img" aria-label="Brake disc with red caliper"></div>
    <div class="title-band">REWARDS SUPPLIER POINTS STATEMENT</div>
    <div class="photo" style="left:493px;top:262px;width:155px;height:137px;background:linear-gradient(180deg,#a9cde6,#dfeef7 45%,#b9d6e4 60%,#c9a68a)" role="img" aria-label="Poolside lounge chairs by the sea"></div>

    <div class="section-title" style="top:412px"><span>::</span> FRANCHISE ACTIVITY <span>::</span></div>

    <div class="data-table" style="left:44px;top:436px;width:559px;height:89px">
      <table class="franchise-table">
        <colgroup><col style="width:62px"><col style="width:132px"><col span="12"></colgroup>
        <tr><th class="left">ACTIVITY BY<br>FRANCHISE</th><th class="left">PTS<br>BALANCE</th><th>Jan</th><th>Feb</th><th>Mar</th><th>Apr</th><th>May</th><th>Jun</th><th>Jul</th><th>Aug</th><th>Sep</th><th>Oct</th><th>Nov</th><th>Dec</th></tr>
        <tr><td class="brand">NORTHWAY</td><td class="label">Points Purchased</td><td>1000</td><td>---</td><td>1000</td><td>---</td><td>---</td><td>1000</td><td>---</td><td>---</td><td>---</td><td>---</td><td>---</td><td>---</td></tr>
        <tr><td></td><td class="label">Points Assigned</td><td>500</td><td>500</td><td>500</td><td>500</td><td>---</td><td>---</td><td>1000</td><td>---</td><td>---</td><td>---</td><td>---</td><td>---</td></tr>
        <tr><td></td><td class="label">Points Purchase Recommendation*</td><td>---</td><td>---</td><td>---</td><td>---</td><td>---</td><td>---</td><td>---</td><td>2000</td><td>---</td><td>2000</td><td>---</td><td>2000</td></tr>
      </table>
    </div>

    <div class="card" style="left:44px;top:541px;width:559px;height:176px">
      <div class="card-title" style="top:15px;font-size:9px">Franchise Point Activity</div>
      <svg class="abs" style="left:0;top:0" width="559" height="176">
        <g font-size="6" fill="#555">
          <text transform="translate(33,46) rotate(90)">Oct</text>
          <text transform="translate(33,68) rotate(90)">Jul</text>
          <text transform="translate(33,86) rotate(90)">Apr</text>
          <text transform="translate(33,104) rotate(90)">Jan</text>
        </g>
        <g stroke="var(--gold)" stroke-width="1.2"><line x1="41" y1="42" x2="425" y2="42"/><line x1="41" y1="55" x2="425" y2="55"/><line x1="41" y1="69" x2="425" y2="69"/></g>
        <g stroke="var(--orange)" stroke-width="1.2"><line x1="41" y1="77" x2="233" y2="77"/><line x1="41" y1="83" x2="233" y2="83"/><line x1="41" y1="97" x2="137" y2="97"/><line x1="41" y1="104" x2="233" y2="104"/><line x1="41" y1="111" x2="137" y2="111"/></g>
        <g stroke="var(--red-dark)" stroke-width="1"><line x1="41" y1="91" x2="137" y2="91"/><line x1="41" y1="108" x2="137" y2="108"/><line x1="41" y1="114" x2="233" y2="114"/></g>
        <g font-size="6" fill="#555">
          <text transform="translate(135,125) rotate(90)">500</text>
          <text transform="translate(231,125) rotate(90)">1,000</text>
          <text transform="translate(327,125) rotate(90)">1,500</text>
          <text transform="translate(423,125) rotate(90)">2,000</text>
          <text transform="translate(519,125) rotate(90)">2,500</text>
        </g>
        <g font-size="6" fill="#555">
          <rect x="158" y="151" width="4" height="4" fill="var(--red-dark)"/><text x="164" y="155">Points Purchased</text>
          <rect x="222" y="151" width="4" height="4" fill="var(--orange)"/><text x="228" y="155">Points Assigned</text>
          <rect x="283" y="151" width="4" height="4" fill="var(--gold)"/><text x="289" y="155">Points Purchase Recommendation*</text>
        </g>
      </svg>
    </div>

    <div class="footer">
      <div class="footer-contact" style="top:36px"><small>TO LEARN MORE</small><b>1.800.555.0142</b> OR SALES@VRELTO.COM</div>
      <div class="footer-brand" style="left:378px;top:35px">
        <div class="brand-dot"></div><div class="brand-name">KEYSTONE PERKS</div><div class="brand-sep"></div><div class="brand-url">VRELTO.COM</div>
      </div>
    </div>

    <div class="card" style="left:44px;top:733px;width:270px;height:135px">
      <div class="card-title" style="top:33px;font-size:7px;font-weight:700">Franchise Point Activity</div>
      <svg class="abs" style="left:0;top:0" width="270" height="135">
        <text x="18" y="60" font-size="4" fill="#555" transform="rotate(-90 18 60)">4,000</text>
        <polyline fill="none" stroke="var(--red-dark)" stroke-width=".8" points="22,74 40,72 60,74 80,70 100,74 120,73 140,70 160,74 180,72 200,74 220,72 240,72"/>
        <polyline fill="none" stroke="var(--orange)" stroke-width=".8" points="22,73 40,73 60,71 80,74 100,73 120,70 140,74 160,71 180,74 200,70 220,74 240,67 252,65"/>
        <polyline fill="none" stroke="var(--gold)" stroke-width=".8" points="22,75 40,74 60,75 80,75 100,74 120,75 140,72 160,76 180,72 200,76 220,71 240,75 252,70"/>
        <g font-size="4" fill="#555">
          <text x="20" y="84">Jan</text><text x="60" y="84">Mar</text><text x="100" y="84">May</text><text x="140" y="84">Jul</text><text x="180" y="84">Sep</text><text x="220" y="84">Nov</text>
          <text x="64" y="97">— Points Purchased</text><text x="108" y="97">— Points Assigned</text><text x="150" y="97">— Points Purchase Recommendation*</text>
        </g>
      </svg>
    </div>

    <div class="card" style="left:335px;top:733px;width:269px;height:135px">
      <div class="card-title" style="top:13px;font-size:7px">Chart Title</div>
      <svg class="abs" style="left:0;top:0" width="269" height="135">
        <g font-size="4.5" fill="#555">
          <text transform="translate(36,35) rotate(90)">Oct</text><text transform="translate(36,47) rotate(90)">Jul</text>
          <text transform="translate(36,57) rotate(90)">Apr</text><text transform="translate(36,67) rotate(90)">Jan</text>
        </g>
        <g stroke="var(--gold)" stroke-width=".9"><line x1="44" y1="33" x2="196" y2="33"/><line x1="44" y1="42" x2="196" y2="42"/><line x1="44" y1="50" x2="196" y2="50"/></g>
        <g stroke="var(--orange)" stroke-width=".9"><line x1="44" y1="55" x2="120" y2="55"/><line x1="44" y1="60" x2="82" y2="60"/><line x1="44" y1="66" x2="120" y2="66"/><line x1="44" y1="71" x2="82" y2="71"/></g>
        <g font-size="4.5" fill="#555">
          <text transform="translate(82,84) rotate(90)">500</text><text transform="translate(120,84) rotate(90)">1,000</text>
          <text transform="translate(158,84) rotate(90)">1,500</text><text transform="translate(196,84) rotate(90)">2,000</text><text transform="translate(234,84) rotate(90)">2,500</text>
          <rect x="66" y="109" width="3" height="3" fill="var(--red-dark)"/><text x="71" y="112">Points Purchased</text>
          <rect x="160" y="109" width="3" height="3" fill="var(--orange)"/><text x="165" y="112">Points Assigned</text>
          <rect x="66" y="116" width="3" height="3" fill="var(--gold)"/><text x="71" y="119">Points Purchase Recommendation*</text>
        </g>
      </svg>
    </div>
  </section>

  <section class="page page--summary">
    <div class="section-title" style="top:20px"><span>::</span> MARKET SUMMARY <span>::</span></div>

    <div class="data-table" style="left:45px;top:44px;width:559px;height:90px">
      <table class="market-table">
        <colgroup><col style="width:85px"><col span="12"></colgroup>
        <tr><th class="left">OH_Cleveland</th><th>Jan</th><th>Feb</th><th>Mar</th><th>Apr</th><th>May</th><th>Jun</th><th>Jul</th><th>Aug</th><th>Sep</th><th>Oct</th><th>Nov</th><th>Dec</th></tr>
        <tr><td class="left">Pts Balance</td><td>700</td><td>---</td><td>500</td><td>---</td><td>250</td><td>---</td><td>83.3</td><td>83.3</td><td>83.3</td><td>83.3</td><td>83.3</td><td>83.3</td></tr>
        <tr><td class="left">Pts Assigned</td><td>300</td><td>500</td><td>200</td><td>300</td><td>250</td><td>200</td><td>200</td><td>175</td><td>150</td><td>125</td><td>100</td><td>100</td></tr>
        <tr><td class="left">Pts Purchased</td><td>1000</td><td>100</td><td>500</td><td>100</td><td>200</td><td>300</td><td>400</td><td>500</td><td>600</td><td>700</td><td>800</td><td>800</td></tr>
      </table>
    </div>

    <div class="card" style="left:45px;top:150px;width:269px;height:135px">
      <div class="card-title" style="top:22px;font-size:5px">Market Summary</div>
      <svg class="abs" style="left:0;top:0" width="269" height="135">
        <g font-size="4" fill="#555"><text transform="translate(22,40) rotate(90)">1,000</text><text transform="translate(22,56) rotate(90)">500</text><text transform="translate(22,74) rotate(90)">0</text></g>
        <line x1="28" y1="100" x2="246" y2="100" stroke="#ccc" stroke-width=".5"/>
        <polyline fill="none" stroke="var(--gold)" stroke-width=".8" points="30,90 48,80 68,98 88,92 108,96 128,92 148,88 168,86 188,84 208,82 228,80 246,80"/>
        <polyline fill="none" stroke="var(--orange)" stroke-width=".8" points="30,78 48,86 68,95 88,89 108,92 128,95 148,96 168,96 188,96 208,97 228,97 246,97"/>
        <polyline fill="none" stroke="var(--red-dark)" stroke-width=".8" points="30,92 48,100 68,92 88,100 108,96 128,100 148,98 168,98 188,98 208,98 228,98 246,98"/>
        <g font-size="3.5" fill="#555">
          <text transform="translate(30,104) rotate(90)">Jan</text><text transform="translate(50,104) rotate(90)">Feb</text><text transform="translate(70,104) rotate(90)">Mar</text><text transform="translate(90,104) rotate(90)">Apr</text><text transform="translate(110,104) rotate(90)">May</text><text transform="translate(130,104) rotate(90)">Jun</text><text transform="translate(150,104) rotate(90)">Jul</text><text transform="translate(170,104) rotate(90)">Aug</text><text transform="translate(190,104) rotate(90)">Sep</text><text transform="translate(210,104) rotate(90)">Oct</text><text transform="translate(230,104) rotate(90)">Nov</text><text transform="translate(246,104) rotate(90)">Dec</text>
        </g>
      </svg>
    </div>

    <div class="card" style="left:335px;top:150px;width:270px;height:135px">
      <svg class="abs" style="left:0;top:0" width="270" height="135">
        <g font-size="5" fill="#555"><text transform="translate(36,18) rotate(90)">Pts Purchased</text><text transform="translate(36,69) rotate(90)">Pts Balance</text></g>
        <rect x="48" y="55" width="178" height="7" fill="var(--red-dark)"/><text x="229" y="61" font-size="5" fill="#333">1,000</text>
        <rect x="48" y="77" width="54" height="7" fill="var(--red-dark)"/><text x="105" y="83" font-size="5" fill="#333">300</text>
        <rect x="48" y="99" width="125" height="7" fill="var(--red-dark)"/><text x="176" y="105" font-size="5" fill="#333">700</text>
      </svg>
    </div>

    <div class="section-title" style="top:314px"><span>::</span> SHOP REDEMPTION <span>::</span></div>
    <div class="section-sub" style="top:333px">Shop Redemption Summary</div>

    <div class="data-table" style="left:45px;top:355px;width:559px;height:185px">
      <table class="shop-table">
        <colgroup><col style="width:178px"><col style="width:186px"><col></colgroup>
        <tr><th class="left">SHOP NAME</th><th>PTS.REDEEMED</th><th>PRODUCT / DESCRIPTION</th></tr>
        <tr><td class="left">Harlan's Collision Center, Barberton</td><td>488</td><td>Shopwell.com $100 E-Card</td></tr>
        <tr><td class="left">Precision Auto Works Inc, North Royalton</td><td>122</td><td>Hardline $100 E-Card</td></tr>
        <tr><td class="left">Ironside Auto Body - Willowwick, Willowick</td><td>122</td><td>Shopwell.com $100 E-Card</td></tr>
        <tr><td class="left">Marlow's Body Shop, Akron</td><td>122</td><td>Shopwell.com $100 E-Card</td></tr>
        <tr><td class="left">Parkside Auto Body, Richfield</td><td>62</td><td>Hardline $50 Gift Card</td></tr>
        <tr><td class="left">Precision Auto Works Inc, North Royalton</td><td>61</td><td>Hardline $50 E-Card</td></tr>
        <tr><td class="left">Marlow's Body Shop, Akron</td><td>61</td><td>Shopwell.com $50 E-Card</td></tr>
        <tr><td class="left">Ironside Auto Body - Willowwick, Willowick</td><td>31</td><td>Shopwell.com $25 E-Card</td></tr>
        <tr><td class="left">Parkside Auto Body, Richfield</td><td>31</td><td>Hardline $25 Gift Card</td></tr>
        <tr><td class="left">Ironside Auto Body - Willowwick, Willowick</td><td>6</td><td>Shopwell.com $5 E-Card</td></tr>
      </table>
    </div>

    <div class="footer">
      <div class="footer-contact" style="top:76px"><small>TO LEARN MORE</small><b>1.800.555.0142</b> OR SALES@VRELTO.COM</div>
      <div class="footer-brand" style="left:377px;top:72px">
        <div class="brand-dot"></div><div class="brand-name">KEYSTONE PERKS</div><div class="brand-sep"></div><div class="brand-url">VRELTO.COM</div>
      </div>
    </div>

    <div class="card" style="left:45px;top:559px;width:558px;height:289px;background:#e9e9e9;border-radius:22px">
      <svg class="abs" style="left:0;top:0" width="558" height="289">
        <text x="36" y="20" font-size="4.5" fill="#555">Supplier Activity Summary</text>
        <rect x="36" y="22" width="493" height="7" fill="var(--red)"/>
        <g font-size="4.5" fill="#fff"><text x="38" y="27.5">SUPPLIER</text><text x="115" y="27.5">Balance</text><text x="200" y="27.5">Jan</text><text x="228" y="27.5">Feb</text><text x="256" y="27.5">Mar</text><text x="284" y="27.5">Apr</text><text x="312" y="27.5">May</text><text x="340" y="27.5">Jun</text><text x="368" y="27.5">Jul</text><text x="396" y="27.5">Aug</text><text x="422" y="27.5">Sep</text><text x="450" y="27.5">Oct</text><text x="478" y="27.5">Nov</text><text x="504" y="27.5">Dec</text></g>
        <line x1="280" y1="14" x2="280" y2="280" stroke="#bbb" stroke-width=".5"/>
        <g font-size="3.8" fill="#555">
          <text x="38" y="36">Dalton Motor Group</text>
          <text x="38" y="50.4">Garvey Motors CDJR</text>
          <text x="38" y="64.8">Garvey Motors East</text>
          <text x="38" y="79.2">Garvey Motors West</text>
          <text x="38" y="93.6">Bedford Import Center</text>
          <text x="38" y="108">Bedford Luxury Motors</text>
          <text x="38" y="122.4">Metro Prestige Motors</text>
          <text x="38" y="136.8">Vantage Motors</text>
        </g>
        <g font-size="3.8" fill="#555" text-anchor="end">
          <text x="154" y="36">15</text><text x="154" y="50.4">18</text><text x="154" y="64.8">1,971</text><text x="154" y="79.2">450</text><text x="154" y="108">675</text><text x="154" y="122.4">100</text><text x="154" y="136.8">502</text>
        </g>
        <g font-size="3.8" fill="#555">
          <text x="157" y="36">Points Purchased</text><text x="157" y="43.2">Points Assigned</text>
          <text x="157" y="50.4">Points Purchased</text><text x="157" y="57.6">Points Assigned</text>
          <text x="157" y="64.8">Points Purchased</text><text x="157" y="72">Points Assigned</text>
          <text x="157" y="79.2">Points Purchased</text><text x="157" y="86.4">Points Assigned</text>
          <text x="157" y="93.6">Points Purchased</text><text x="157" y="100.8">Points Assigned</text>
          <text x="157" y="108">Points Purchased</text><text x="157" y="115.2">Points Assigned</text>
          <text x="157" y="122.4">Points Purchased</text><text x="157" y="129.6">Points Assigned</text>
          <text x="157" y="136.8">Points Purchased</text><text x="157" y="144">Points Assigned</text>
          <text x="298" y="72">168</text><text x="270" y="79.2">500</text><text x="320" y="79.2">500</text><text x="320" y="86.4">610</text>
          <text x="216" y="115.2">11</text><text x="290" y="144">2,018</text><text x="320" y="136.8">500</text>
        </g>
        <g font-size="3.8" fill="#555">
          <text x="36" y="165">Total Suppliers</text><text x="146" y="165">20</text>
          <text x="36" y="172">Suppliers Enrolled</text><text x="146" y="172">8</text>
          <text x="36" y="179">Suppliers Assigned Pts</text><text x="146" y="179">4</text>
          <text x="36" y="186">Suppliers Purchased Pts</text><text x="146" y="186">2</text>
          <text transform="translate(198,208) rotate(90)">Total Suppliers</text>
        </g>
        <rect x="213" y="181" width="17" height="6" fill="var(--red-dark)"/><text x="233" y="186" font-size="4" fill="#333">2</text>
        <rect x="213" y="202" width="35" height="6" fill="var(--red-dark)"/><text x="251" y="207" font-size="4" fill="#333">4</text>
        <rect x="213" y="223" width="70" height="6" fill="var(--red-dark)"/><text x="286" y="228" font-size="4" fill="#333">8</text>
        <rect x="213" y="244" width="178" height="6" fill="var(--red-dark)"/><text x="394" y="249" font-size="4" fill="#333">20</text>
      </svg>
    </div>
  </section>

</div>
</body>
</html>
```